Survey App for phone users trying a new phone with Dual connectivity

Survey App Brief<br/>Design For an Android Survey App for users' feedback on Call, SMS, Data and Streaming Experience on their Mobile phones.<br/><br/>Purpose of the App<br/>To ensure that the user's experience is not impacted by the network switching between two network on the special mobile phones they newly started using.<br/><br/>App Requirements:<br/>First screen: The registration screen, where the user needs to enter the following:<br/>Name: text box<br/>Phone Number: text box<br/>Group Number : <br/><br/>An information text:<br/>By Registering I agree to participate in the Survey.<br/><br/>Register: Button<br/><br/>Start Screen - Survey screens (next time user open the App this will be the first screen):<br/>We need feedback for 4 indicators:<br/>Call Experience<br/>SMS Experience<br/>Data Experience<br/>Streaming Experience<br/><br/>Each Experience can be in the form of a questionnaire or Satisfied/ Somewhat Satisfied / Extremely Satisfied form with radio buttons or on a scale of 1 to 5. We need to ensure that the format used is very professional.<br/><br/>An optional text box for the user to enter the comment in a free format.<br/><br/>This can be done in 4 different screens or in one single screen if it does not give a clumsy look.<br/><br/>A Send button at the end to submit the Survey.<br/><br/>We need a burger menu at the top left corner of this screen, which when expanded will provide 5 options:<br/>Edit User Profile<br/>Survey interval Timer<br/>FAQ<br/>Exit<br/>About<br/><br/><br/>Please ensure that the app is simple, friendly, lively and professional at the same time so that it ignites an interest in the user to use the app.<br/>Use Logo as appropriate.
Industry/Entity Type
Telecommunications
Colors
Designer to choose colors to be used in the design.
Look and feel
Each slider illustrates characteristics of the customer's brand and the style your logo design should communicate.

```html
<!DOCTYPE html>
<html lang="en">
<head>
<meta charset="utf-8">
<title>Meridian Signal Survey App</title>
<link rel="stylesheet" href="https://fonts.googleapis.com/css2?family=Open+Sans:wght@400;600;700&family=Montserrat:wght@500;600&display=swap">
<style>
:root{
  --bg-blue:#4a90e0;
  --bg-blue-deep:#3f84d6;
  --white:#ffffff;
  --screen:#fdfdff;
  --ink:#2b3151;
  --ink-soft:#5a6690;
  --muted:#a3a6b3;
  --field:#f3f4fa;
  --note:#e6e8f0;
  --card:#f7f8fc;
  --card-line:#e7e9f2;
  --accent:#2f80dc;
  --accent-text:#2f8be0;
  --button:#3fa9e0;
  --track-off:#dadbe0;
  --logo-ink:#7c7f88;
  --logo-dot:#6ec6f0;
  --dim:#c9c9cd;
  --dim-card:#c1c2c7;
}
*{box-sizing:border-box;margin:0;padding:0}
html,body{width:1200px;height:2410px;overflow:hidden}
body{position:relative;background:var(--bg-blue);font-family:"Open Sans",Arial,sans-serif;color:var(--ink)}
.backdrop{position:absolute;left:0;top:0;width:1200px;height:2410px}
.brand{position:absolute;display:flex;align-items:center;gap:14px;color:var(--logo-ink);font-weight:600;line-height:1}
.brand-dot{border-radius:50%;background:var(--logo-dot);flex:none}
.brand-name{letter-spacing:.06em;text-transform:uppercase}
.brand-name span{display:block}
.brand-hero{left:420px;top:112px}
.brand-hero .brand-dot{width:104px;height:104px}
.brand-hero .brand-name{font-size:34px}
.brand-hero .brand-name span+span{margin-top:6px}
.brand-sm{gap:7px;left:50%;transform:translateX(-50%)}
.brand-sm .brand-dot{width:30px;height:30px}
.brand-sm .brand-name{font-size:10px}
.brand-sm .brand-name span+span{margin-top:2px}
.brand-md .brand-dot{width:50px;height:50px}
.brand-md .brand-name{font-size:15px}

.screen{position:absolute;background:var(--screen);overflow:hidden;box-shadow:0 6px 24px rgba(20,50,110,.12)}
.status{position:absolute;left:0;top:0;width:100%;height:46px}
.status-time{position:absolute;left:36px;top:16px;font-size:15px;font-weight:600;color:#111}
.status-icons{position:absolute;right:18px;top:18px}
.home-bar{position:absolute;width:148px;height:5px;border-radius:3px;background:#111;left:50%;transform:translateX(-50%)}

.register{left:157px;top:348px;width:416px;height:902px}
.register-title{position:absolute;left:22px;top:176px;font-size:31px;font-weight:700;color:var(--ink)}
.field{position:absolute;left:16px;width:385px;height:54px;border-radius:27px;background:var(--field);display:flex;align-items:center;padding-left:28px;gap:20px;font-size:18px;color:var(--ink-soft)}
.field svg{flex:none}
.agree{position:absolute;left:40px;width:336px;top:703px;text-align:center;font-size:15.5px;line-height:21px;color:#6f7ab8}
.btn{position:absolute;left:22px;width:371px;height:54px;border-radius:27px;background:var(--button);color:var(--white);font-size:15px;font-weight:600;letter-spacing:.03em;display:flex;align-items:center;justify-content:center}

.survey{left:672px;top:348px;width:417px;height:1250px}
.burger{position:absolute;left:21px;top:65px}
.survey-lead{position:absolute;left:0;width:100%;top:116px;text-align:center;font-size:16px;font-weight:600;color:#222}
.card{position:absolute;left:16px;width:385px;height:230px;border-radius:28px;background:var(--card);border:1px solid var(--card-line)}
.card-title{position:absolute;left:25px;top:24px;font-size:18px;font-weight:600;color:#2a2d38}
.scale{position:absolute;left:0;top:55px}
.scale-labels{position:absolute;left:0;top:107px;width:385px;height:20px;font-size:14px;color:var(--muted)}
.scale-labels span{position:absolute;transform:translateX(-50%);white-space:nowrap}
.scale-labels .on{color:var(--accent-text);font-weight:600}
.note{position:absolute;left:19px;top:161px;width:348px;height:49px;border-radius:25px;background:var(--note);font-size:14px;color:#6b7090;display:flex;align-items:center;padding-left:25px}
.survey .btn{left:16px;width:385px;height:55px;top:1135px}

.drawer-screen{left:157px;top:1386px;width:416px;height:902px;background:var(--dim)}
.drawer-behind{position:absolute;left:347px;top:0;width:69px;height:100%;overflow:hidden}
.behind-card{position:absolute;left:15px;width:385px;height:230px;border-radius:28px;background:var(--dim-card)}
.behind-card .t{position:absolute;left:26px;top:22px;font-size:18px;font-weight:600;color:#3d404c}
.behind-card .bar{position:absolute;left:26px;top:68px;width:80px;height:8px;border-radius:4px;background:#2f7acb}
.behind-card .p{position:absolute;left:26px;top:108px;font-size:14px;color:#4c4f5b}
.behind-card .n{position:absolute;left:19px;top:161px;width:348px;height:49px;border-radius:25px;background:#b3b4ba;font-size:14px;color:#50535f;padding:15px 25px}
.drawer{position:absolute;left:0;top:0;width:347px;height:100%;background:var(--screen)}
.menu{list-style:none;position:absolute;left:0;top:0;width:100%}
.menu-item{position:absolute;left:7px;width:328px;height:55px;display:flex;align-items:center;padding-left:38px;gap:20px;font-family:"Montserrat",Arial,sans-serif;font-size:16px;font-weight:600;color:var(--ink)}
.menu-item.active{border:1px solid #e3e6f2;background:#f6f7fc;border-radius:28px;color:var(--accent-text)}
</style>
</head>
<body>

<svg class="backdrop" viewBox="0 0 1200 2410" aria-hidden="true">
  <circle cx="1420" cy="1545" r="490" fill="var(--bg-blue-deep)"/>
  <ellipse cx="90" cy="1000" rx="520" ry="320" fill="#468bdc"/>
  <path d="M0 0H1200V383Q600 760 0 383Z" fill="var(--white)"/>
</svg>

<div class="brand brand-hero">
  <span class="brand-dot"></span>
  <span class="brand-name"><span>Meridian</span><span>Signal</span></span>
</div>

<!-- Registration screen -->
<section class="screen register">
  <div class="status">
    <span class="status-time">9:41</span>
    <svg class="status-icons" width="74" height="12" viewBox="0 0 74 12"><rect x="0" y="8" width="3" height="4" rx="1" fill="#111"/><rect x="5" y="6" width="3" height="6" rx="1" fill="#111"/><rect x="10" y="3" width="3" height="9" rx="1" fill="#111"/><rect x="15" y="0" width="3" height="12" rx="1" fill="#111"/><path d="M26 4a10 10 0 0 1 14 0M29 7a6 6 0 0 1 8 0" stroke="#111" stroke-width="2" fill="none" stroke-linecap="round"/><circle cx="33" cy="10.5" r="1.6" fill="#111"/><rect x="48" y="1" width="22" height="10" rx="3" fill="none" stroke="#999"/><rect x="50" y="3" width="18" height="6" rx="1.5" fill="#111"/><rect x="71" y="4" width="2" height="4" rx="1" fill="#999"/></svg>
  </div>
  <div class="brand brand-sm brand-md" style="top:100px">
    <span class="brand-dot"></span>
    <span class="brand-name"><span>Meridian</span><span>Signal</span></span>
  </div>
  <h1 class="register-title">Registration.</h1>
  <div class="field" style="top:257px">
    <svg width="22" height="22" viewBox="0 0 22 22" fill="none" stroke="#6f7ab8" stroke-width="1.5"><circle cx="11" cy="7" r="5"/><path d="M2 21c0-5 4-8 9-8s9 3 9 8z"/></svg>Name
  </div>
  <div class="field" style="top:335px">
    <svg width="22" height="22" viewBox="0 0 22 22" fill="none" stroke="#6f7ab8" stroke-width="1.5" stroke-linejoin="round"><path d="M4 2l4 1 1 5-3 2c1 3 3 5 6 6l2-3 5 1 1 4c-1 2-3 3-5 2C10 18 5 13 3 7 2 5 2 3 4 2z"/></svg>Phone Number
  </div>
  <div class="field" style="top:413px">
    <svg width="22" height="22" viewBox="0 0 22 22" fill="none" stroke="#6f7ab8" stroke-width="1.5"><circle cx="9" cy="7" r="5"/><path d="M1 20c0-5 3-7 8-7s8 2 8 7z"/><path d="M14 3a4 4 0 0 1 0 8M18 14c2 1 3 3 3 6"/></svg>Group Number
  </div>
  <p class="agree">By Registering I agree to participate in the Survey</p>
  <div class="btn" style="top:768px">REGISTER</div>
  <span class="home-bar" style="top:886px"></span>
</section>

<!-- Survey screen -->
<section class="screen survey">
  <div class="status">
    <span class="status-time">9:41</span>
    <svg class="status-icons" width="74" height="12" viewBox="0 0 74 12"><rect x="0" y="8" width="3" height="4" rx="1" fill="#111"/><rect x="5" y="6" width="3" height="6" rx="1" fill="#111"/><rect x="10" y="3" width="3" height="9" rx="1" fill="#111"/><rect x="15" y="0" width="3" height="12" rx="1" fill="#111"/><path d="M26 4a10 10 0 0 1 14 0M29 7a6 6 0 0 1 8 0" stroke="#111" stroke-width="2" fill="none" stroke-linecap="round"/><circle cx="33" cy="10.5" r="1.6" fill="#111"/><rect x="48" y="1" width="22" height="10" rx="3" fill="none" stroke="#999"/><rect x="50" y="3" width="18" height="6" rx="1.5" fill="#111"/><rect x="71" y="4" width="2" height="4" rx="1" fill="#999"/></svg>
  </div>
  <svg class="burger" width="30" height="24" viewBox="0 0 30 24" stroke="#2b3151" stroke-width="2.4" stroke-linecap="round"><path d="M1 2h28M1 12h28M1 22h28"/></svg>
  <div class="brand brand-sm" style="top:60px">
    <span class="brand-dot"></span>
    <span class="brand-name"><span>Meridian</span><span>Signal</span></span>
  </div>
  <p class="survey-lead">We need feedback for survey</p>

  <article class="card" style="top:160px">
    <h2 class="card-title">Call Experience</h2>
    <svg class="scale" width="385" height="50" viewBox="0 0 385 50" font-family="Open Sans, sans-serif" font-size="14" text-anchor="middle">
      <path d="M195 22H348" stroke="var(--track-off)" stroke-width="8"/>
      <path d="M40 22H195" stroke="var(--accent)" stroke-width="8"/>
      <g fill="#fff" stroke-width="3"><circle cx="40" cy="22" r="14" stroke="var(--accent)"/><circle cx="117" cy="22" r="14" stroke="var(--accent)"/><circle cx="195" cy="22" r="14" stroke="var(--accent)"/><circle cx="271" cy="22" r="13" stroke="var(--track-off)"/><circle cx="348" cy="22" r="13" stroke="var(--track-off)"/></g>
      <g font-weight="600"><text x="40" y="27" fill="var(--accent)">1</text><text x="117" y="27" fill="var(--accent)">2</text><text x="195" y="27" fill="var(--accent)">3</text><text x="271" y="27" fill="#c8c8cc">4</text><text x="348" y="27" fill="#c8c8cc">5</text></g>
    </svg>
    <div class="scale-labels"><span style="left:40px">Poor</span><span style="left:117px">Not Well</span><span class="on" style="left:198px">Neutral</span><span style="left:273px">Satisfied</span><span style="left:348px">Great</span></div>
    <div class="note">Note for feedback</div>
  </article>

  <article class="card" style="top:401px">
    <h2 class="card-title">SMS Experience</h2>
    <svg class="scale" width="385" height="50" viewBox="0 0 385 50" font-family="Open Sans, sans-serif" font-size="14" text-anchor="middle">
      <path d="M271 22H348" stroke="var(--track-off)" stroke-width="8"/>
      <path d="M40 22H271" stroke="var(--accent)" stroke-width="8"/>
      <g fill="#fff" stroke-width="3"><circle cx="40" cy="22" r="14" stroke="var(--accent)"/><circle cx="117" cy="22" r="14" stroke="var(--accent)"/><circle cx="195" cy="22" r="14" stroke="var(--accent)"/><circle cx="271" cy="22" r="14" stroke="var(--accent)"/><circle cx="348" cy="22" r="13" stroke="var(--track-off)"/></g>
      <g font-weight="600"><text x="40" y="27" fill="var(--accent)">1</text><text x="117" y="27" fill="var(--accent)">2</text><text x="195" y="27" fill="var(--accent)">3</text><text x="271" y="27" fill="var(--accent)">4</text><text x="348" y="27" fill="#c8c8cc">5</text></g>
    </svg>
    <div class="scale-labels"><span style="left:40px">Poor</span><span style="left:117px">Not Well</span><span style="left:197px">Neutral</span><span class="on" style="left:273px">Satisfied</span><span style="left:348px">Great</span></div>
    <div class="note">Note for feedback</div>
  </article>

  <article class="card" style="top:643px">
    <h2 class="card-title">Data Experience</h2>
    <svg class="scale" width="385" height="50" viewBox="0 0 385 50" font-family="Open Sans, sans-serif" font-size="14" text-anchor="middle">
      <path d="M271 22H348" stroke="var(--track-off)" stroke-width="8"/>
      <path d="M40 22H271" stroke="var(--accent)" stroke-width="8"/>
      <g fill="#fff" stroke-width="3"><circle cx="40" cy="22" r="14" stroke="var(--accent)"/><circle cx="117" cy="22" r="14" stroke="var(--accent)"/><circle cx="195" cy="22" r="14" stroke="var(--accent)"/><circle cx="271" cy="22" r="14" stroke="var(--accent)"/><circle cx="348" cy="22" r="13" stroke="var(--track-off)"/></g>
      <g font-weight="600"><text x="40" y="27" fill="var(--accent)">1</text><text x="117" y="27" fill="var(--accent)">2</text><text x="195" y="27" fill="var(--accent)">3</text><text x="271" y="27" fill="var(--accent)">4</text><text x="348" y="27" fill="#c8c8cc">5</text></g>
    </svg>
    <div class="scale-labels"><span style="left:40px">Poor</span><span style="left:117px">Not Well</span><span style="left:197px">Neutral</span><span class="on" style="left:273px">Satisfied</span><span style="left:348px">Great</span></div>
    <div class="note">Note for feedback</div>
  </article>

  <article class="card" style="top:885px">
    <h2 class="card-title">Streaming Experience</h2>
    <svg class="scale" width="385" height="50" viewBox="0 0 385 50" font-family="Open Sans, sans-serif" font-size="14" text-anchor="middle">
      <path d="M40 22H348" stroke="var(--accent)" stroke-width="8"/>
      <g fill="#fff" stroke-width="3" stroke="var(--accent)"><circle cx="40" cy="22" r="14"/><circle cx="117" cy="22" r="14"/><circle cx="195" cy="22" r="14"/><circle cx="271" cy="22" r="14"/><circle cx="348" cy="22" r="14"/></g>
      <g font-weight="600" fill="var(--accent)"><text x="40" y="27">1</text><text x="117" y="27">2</text><text x="195" y="27">3</text><text x="271" y="27">4</text><text x="348" y="27">5</text></g>
    </svg>
    <div class="scale-labels"><span style="left:40px">Poor</span><span style="left:117px">Not Well</span><span style="left:197px">Neutral</span><span style="left:273px">Satisfied</span><span class="on" style="left:348px">Great</span></div>
    <div class="note">Note for feedback</div>
  </article>

  <div class="btn">SUBMIT</div>
  <span class="home-bar" style="top:1236px"></span>
</section>

<!-- Menu drawer screen -->
<section class="screen drawer-screen">
  <div class="drawer-behind">
    <svg style="position:absolute;left:22px;top:64px" width="30" height="24" viewBox="0 0 30 24" stroke="#2b3151" stroke-width="2.4" stroke-linecap="round"><path d="M1 2h28M1 12h28M1 22h28"/></svg>
    <div class="behind-card" style="top:162px"><span class="t">Call Experience</span><span class="bar"></span><span class="p">Poor</span><span class="n">Note for feedback</span></div>
    <div class="behind-card" style="top:404px"><span class="t">SMS Experience</span><span class="bar"></span><span class="p">Poor</span><span class="n">Note for feedback</span></div>
    <div class="behind-card" style="top:646px"><span class="t">Data Experience</span><span class="bar"></span><span class="p">Poor</span><span class="n">Note for feedback</span></div>
    <div class="behind-card" style="top:888px"></div>
  </div>
  <div class="status">
    <span class="status-time">9:41</span>
    <svg class="status-icons" width="74" height="12" viewBox="0 0 74 12"><rect x="0" y="8" width="3" height="4" rx="1" fill="#111"/><rect x="5" y="6" width="3" height="6" rx="1" fill="#111"/><rect x="10" y="3" width="3" height="9" rx="1" fill="#111"/><rect x="15" y="0" width="3" height="12" rx="1" fill="#111"/><path d="M26 4a10 10 0 0 1 14 0M29 7a6 6 0 0 1 8 0" stroke="#111" stroke-width="2" fill="none" stroke-linecap="round"/><circle cx="33" cy="10.5" r="1.6" fill="#111"/><rect x="48" y="1" width="22" height="10" rx="3" fill="none" stroke="#999"/><rect x="50" y="3" width="18" height="6" rx="1.5" fill="#111"/><rect x="71" y="4" width="2" height="4" rx="1" fill="#999"/></svg>
  </div>
  <nav class="drawer">
    <div class="status"><span class="status-time">9:41</span></div>
    <div class="brand brand-sm" style="top:68px">
      <span class="brand-dot"></span>
      <span class="brand-name"><span>Meridian</span><span>Signal</span></span>
    </div>
    <ul class="menu">
      <li class="menu-item" style="top:125px">
        <svg width="16" height="16" viewBox="0 0 16 16" fill="none" stroke="#2b3151" stroke-width="1.3"><rect x="1" y="1" width="5.5" height="5.5"/><rect x="9.5" y="1" width="5.5" height="5.5"/><rect x="1" y="9.5" width="5.5" height="5.5"/><rect x="9.5" y="9.5" width="5.5" height="5.5"/></svg>Dashboard</li>
      <li class="menu-item" style="top:191px">
        <svg width="16" height="16" viewBox="0 0 16 16" fill="none" stroke="#2b3151" stroke-width="1.3"><path d="M7 2H2v12h12V9"/><path d="M12 1.5l2.5 2.5L8 10.5H5.5V8z"/></svg>Edit Profiles</li>
      <li class="menu-item active" style="top:262px">
        <svg width="16" height="16" viewBox="0 0 16 16" fill="none" stroke="#2f8be0" stroke-width="1.4" stroke-linecap="round"><path d="M1 11l4-4 3 3 7-6"/></svg>Survey interval Timer</li>
      <li class="menu-item" style="top:332px">
        <svg width="16" height="16" viewBox="0 0 16 16" fill="none" stroke="#2b3151" stroke-width="1.3"><circle cx="3" cy="8" r="2"/><circle cx="13" cy="3" r="2"/><circle cx="13" cy="13" r="2"/><path d="M5 7l6-3M5 9l6 3"/></svg>Share this App</li>
      <li class="menu-item" style="top:403px">
        <svg width="16" height="16" viewBox="0 0 16 16" fill="none" stroke="#2b3151" stroke-width="1.3"><rect x="1" y="3" width="14" height="10"/><path d="M1 3l7 6 7-6"/></svg>Contact Us</li>
      <li class="menu-item" style="top:473px">
        <svg width="16" height="16" viewBox="0 0 16 16" fill="none" stroke="#2b3151" stroke-width="1.3"><circle cx="8" cy="8" r="7"/><circle cx="8" cy="8" r="3"/><path d="M3 3l3 3M13 3l-3 3M3 13l3-3M13 13l-3-3"/></svg>Help</li>
      <li class="menu-item" style="top:552px">
        <svg width="16" height="16" viewBox="0 0 16 16" fill="none" stroke="#2b3151" stroke-width="1.3"><path d="M6 2h8v12H6"/><path d="M1 8h8M6 5l3 3-3 3"/></svg>Exit</li>
    </ul>
  </nav>
</section>

</body>
</html>
```